Business Card Design for Kidvale (Hires out childrens play areas)

Looking to have a business card designed for a company we just bought. The company rents out childrens play areas.

I have uploaded a couple of examples of the kind of business card style I like. Here are two more examples:

https://quorvastudio.nz/project/bright-romp-branding/
https://imgvaultcdn.com/design_img/8841052/302917/302917_5518203_8841052_b73e19a2_image.jpg

I think a white card will be best due to all the colours in the logo.

Size we require: 3.75" x 2.25" (horizontally orientated) with a 0.125" bleed

Uploaded is two versions of our logo.

Details for the card:
1. My name: Liam Verster
2. Title: Managing Director
3. Phone no: 021 563 417
4. Email: liam@kidvale.co.nz
5. URL: www.kidvale.co.nz
6. Address:
PO Box 318625
Fernlea, Auckland

Let me know if you need anything else.

Target Market(s)

Hospitals, doctors surgeries, bed shops, etc.

Contact Information for Business Card

Details for the card:
1. My name: Liam Verster
3. Phone no: 021 563 417
5. URL: www.kidvale.co.nz
6. Address:
PO Box 318625
Fernlea, Auckland

Requirements
Should not have
• Not too busy.

```html
<!DOCTYPE html>
<html lang="en">
<head>
<meta charset="utf-8">
<title>Kidvale Business Card</title>
<link href="https://fonts.googleapis.com/css2?family=Arimo:wght@400;700&display=swap" rel="stylesheet">
<style>
  :root {
    --backdrop: #2f3b47;
    --card: #2b2d31;
    --divider: #2a4fa8;
    --name-blue: #2f56b8;
    --text-light: #f2f2f2;
    --brand-accent: #f0a020;
  }
  html, body {
    margin: 0;
    width: 1200px;
    height: 799px;
    overflow: hidden;
    background: var(--backdrop);
    font-family: "Arimo", Arial, sans-serif;
  }
  .business-card {
    position: absolute;
    left: 200px;
    top: 160px;
    width: 800px;
    height: 480px;
    background: var(--card);
    box-shadow: 0 18px 40px rgba(0,0,0,0.35);
  }
  .brand {
    position: absolute;
    left: 110px;
    top: 190px;
    display: flex;
    align-items: center;
    gap: 18px;
  }
  .brand-dot {
    width: 54px;
    height: 54px;
    border-radius: 50%;
    background: var(--brand-accent);
  }
  .brand-name {
    font-size: 64px;
    font-weight: 700;
    color: var(--text-light);
    line-height: 1;
  }
  .divider {
    position: absolute;
    left: 440px;
    top: 70px;
    width: 2px;
    height: 340px;
    background: var(--divider);
  }
  .contact {
    position: absolute;
    left: 480px;
    top: 112px;
    color: var(--text-light);
  }
  .contact-name {
    margin: 0;
    font-size: 27px;
    font-weight: 400;
    color: var(--name-blue);
    line-height: 1;
  }
  .contact-title {
    margin: 2px 0 0;
    font-size: 17px;
    font-weight: 700;
    line-height: 1.2;
  }
  .contact-lines {
    margin: 34px 0 0 12px;
    font-size: 15px;
    font-weight: 700;
    line-height: 1.3;
  }
  .contact-address {
    margin: 26px 0 0 22px;
    font-size: 15px;
    font-weight: 700;
    line-height: 1.3;
  }
</style>
</head>
<body>
  <div class="business-card">
    <div class="brand">
      <span class="brand-dot"></span>
      <span class="brand-name">Kidvale</span>
    </div>
    <div class="divider"></div>
    <div class="contact">
      <h1 class="contact-name">Liam Verster</h1>
      <p class="contact-title">Managing Director</p>
      <p class="contact-lines">021 563 417<br>liam@kidvale.co.nz<br>www.kidvale.co.nz</p>
      <p class="contact-address">PO Box 318625<br>Fernlea, Aukland</p>
    </div>
  </div>
</body>
</html>
```